Flowchart

I need a nice graphic that doesn't look like a stock word/ppt graphic to show the organization of our office. Example included. The idea to get across is that all of the units work together and feed into each other. I need this asap so will likely award tomorrow
Please use all text and if possible incorporate logo.
Design should be around 8.5 X 11 or smaller. Landscape vs. Protrait doesn't matter much.
A few more notes.
no larger than 81/2 by 11
Landscape preferred
Landscape preferred
Landscape

```html
<!DOCTYPE html>
<html lang="en">
<head>
<meta charset="utf-8">
<title>Biosciences Office Organization</title>
<link rel="stylesheet" href="https://fonts.googleapis.com/css2?family=Open+Sans:wght@400;600&display=swap">
<style>
  :root {
    --band-blue: #0a93d8;
    --pill-top: #86cdef;
    --pill-mid: #c4e7f8;
    --pill-bottom: #ffffff;
    --heading-navy: #231c6e;
    --body-ink: #1d1d1d;
    --frame-grey: #9a9a9a;
    --link-blue: #3aa9e2;
    --paper: #ffffff;
  }
  * { box-sizing: border-box; margin: 0; padding: 0; }
  html, body { width: 1200px; height: 815px; overflow: hidden; background: var(--paper); }
  .sheet {
    position: relative;
    width: 1200px;
    height: 815px;
    background: var(--paper);
    border-left: 1px solid var(--frame-grey);
    border-right: 1px solid var(--frame-grey);
    font-family: "Open Sans", "Myriad Pro", sans-serif;
    color: var(--body-ink);
  }
  .band { position: absolute; left: 0; right: 0; height: 20px; background: var(--band-blue); }
  .band--top { top: 0; }
  .band--bottom { bottom: 0; height: 22px; }

  .connectors { position: absolute; inset: 0; pointer-events: none; }

  .unit { position: absolute; left: 0; right: 0; }
  .unit-title {
    position: absolute;
    display: flex;
    align-items: center;
    justify-content: center;
    text-align: center;
    color: var(--heading-navy);
    font-weight: 400;
    font-size: 28px;
    line-height: 1.5;
    letter-spacing: 0.2px;
    border-radius: 999px;
    background: linear-gradient(180deg, var(--pill-top) 0%, var(--pill-mid) 45%, var(--pill-bottom) 100%);
    box-shadow: 8px 8px 9px -4px rgba(0,0,0,0.22);
    white-space: nowrap;
  }
  .unit-points {
    position: absolute;
    left: 75px;
    right: 52px;
    list-style: none;
    font-size: 20px;
    line-height: 30px;
  }
  .unit-points li { position: relative; padding-left: 13px; margin-bottom: 4px; }
  .unit-points li::before {
    content: "";
    position: absolute;
    left: 0; top: 13px;
    width: 6px; height: 6px;
    border-radius: 50%;
    background: var(--body-ink);
  }

  .unit--home .unit-title { top: 58px; left: 372px; width: 466px; height: 52px; }
  .unit--home .unit-points { top: 142px; }

  .unit--committee .unit-title { top: 304px; left: 215px; width: 780px; height: 52px; }
  .unit--committee .unit-points { top: 378px; }

  .unit--office .unit-title { top: 508px; left: 257px; width: 695px; height: 96px; font-size: 29px; line-height: 1.5; }
  .unit--office .unit-points { top: 629px; line-height: 31px; }
  .unit--office .unit-points li { margin-bottom: 6px; }
</style>
</head>
<body>
<main class="sheet">
  <div class="band band--top"></div>

  <svg class="connectors" width="1200" height="815" viewBox="0 0 1200 815" aria-hidden="true">
    <defs>
      <marker id="arrowhead" viewBox="0 0 10 10" refX="8" refY="5" markerWidth="7" markerHeight="7" orient="auto-start-reverse">
        <path d="M0 0 L10 5 L0 10 z" fill="var(--link-blue)"/>
      </marker>
    </defs>
    <g fill="none" stroke="var(--link-blue)" stroke-width="3" stroke-linecap="round">
      <line x1="605" y1="250" x2="605" y2="294" marker-start="url(#arrowhead)" marker-end="url(#arrowhead)"/>
      <line x1="605" y1="450" x2="605" y2="498" marker-start="url(#arrowhead)" marker-end="url(#arrowhead)"/>
      <path d="M1182 84 V556"/>
      <line x1="1182" y1="84" x2="852" y2="84" marker-end="url(#arrowhead)"/>
      <line x1="1182" y1="330" x2="1008" y2="330" marker-end="url(#arrowhead)"/>
      <line x1="1182" y1="556" x2="966" y2="556" marker-end="url(#arrowhead)"/>
    </g>
  </svg>

  <section class="unit unit--home">
    <h2 class="unit-title">Biosciences Home Programs</h2>
    <ul class="unit-points">
      <li>Supports students with department or program specific degree progress and graduation requirements</li>
      <li>Administers program-specific core curriculum</li>
      <li>Eight departments and Six interdisciplinary programs</li>
    </ul>
  </section>

  <section class="unit unit--committee">
    <h2 class="unit-title">Committee on Graduate Admissions &amp; Policy CGAP)</h2>
    <ul class="unit-points">
      <li>Administrative oversight of Biosciences admissions, curriculum and policies</li>
      <li>Forum for cross-program discussion and collaboration</li>
    </ul>
  </section>

  <section class="unit unit--office">
    <h2 class="unit-title">Office of Graduate Education (OGE) &amp; School<br>of Medicine Career Center (SoMCC)</h2>
    <ul class="unit-points">
      <li>Promotes the academic, personal &amp; professional development of all students through comprehensive programs and services</li>
      <li>Advocates for the best possible training and empowerment of all students</li>
      <li>Develops and administers Biosciences – wide,&nbsp; interdisciplinary curriculum</li>
    </ul>
  </section>

  <div class="band band--bottom"></div>
</main>
</body>
</html>
```